Visitenkarten-Design für virtuelle Jobmesse & Jobbörse für Soldaten
Zielgruppe
Die KLO GmbH ist ein Unternehmen das zwei Hauptprodukte betreibt! Zum einen Jobbörse für Soldaten unter www.wachwechselpunkt.de und zum anderen eine virtuelle Jobmesse für Soldaten unter www.marvento.de , die wir zweimal im Jahr veranstalten.
Aufgabenstellung
Wir haben ja die beiden Produkte Wachwechselpunkt.de und die Marvento, für die bereits jeweils ein separtes Logo besteht! Diese finden Sie im Anhang! Beide werden doch jedoch von einem Unternehmen, der KLO GmbH betrieben! Aktuell nutzen wir eine Visitenkarte mit dem Logo von KLO und eine mit dem Logo der MARVENTO. Gerade im Hinblick darauf, dass wir zukünftig auch weiter Plattformen in unser Portfolio aufnehmen, möchte ich hier unsere V-Karten flexibler gestalten!
Ziel soll es also sein, eine Visitenkarte zu gestalten, auf dem klar wird, dass der Mitarbeiter von der KLO GmbH kommt, die KLO GmbH aber unterschiedliche Produkte betreibt.
Im Anhang finden Sie:
1. Das Logo von KLO
2. Das Logo von Marvento
3. Die aktuelle V-Karte von KLO
4. Die aktuelle V-Karte von MARVENTO
Vielleicht ein kleiner Anreiz: Aktuell nutzen wir auch zwei getrennte Geschäftspapiere. Das von www.wachwechselpunkt.de lade ich einmal hoch! Der Designer, der auch die Visitenkarte erstellt, erhällt im Anschluss den 1:1 Auftrag in Höhe von 200 Euro für die Erstellung des Geschäftspapiers! Wenn Sie jetzt schon einen Vorschlag für das Geschäftspapier einreichen, erhöht das natürlich Ihre Chancen, wobei ich verspreche, dass wir im Falle eine Annahme das 1:1 im Anschluß dennoch starten werden!

```html
<!DOCTYPE html>
<html lang="de">
<head>
<meta charset="utf-8">
<title>KLO GmbH – Visitenkarte</title>
<link href="https://fonts.googleapis.com/css2?family=Arimo:wght@400;700&display=swap" rel="stylesheet">
<style>
  :root {
    --brand-blue: #204a7d;
    --text-grey: #808080;
    --paper: #ffffff;
    --edge: #6e6e6e;
  }
  html, body {
    margin: 0;
    padding: 0;
    overflow: hidden;
  }
  body {
    width: 848px;
    height: 1200px;
    background: var(--paper);
    position: relative;
    font-family: "Arimo", Arial, sans-serif;
  }
  p { margin: 0; }
  .card {
    position: absolute;
    top: 198px;
    width: 342px;
    height: 221px;
    box-sizing: border-box;
    overflow: hidden;
  }
  .card--front {
    left: 75px;
    background: var(--paper);
    border: 1px solid var(--edge);
  }
  .card--back {
    left: 437px;
    background: var(--brand-blue);
  }
  .front-arc {
    position: absolute;
    left: 0;
    top: 0;
  }
  .front-arc path { fill: var(--brand-blue); }
  .line {
    position: absolute;
    white-space: nowrap;
    line-height: 1;
  }
  .person-name {
    left: 19px;
    top: 94px;
    font-size: 15.5px;
    font-weight: 700;
    color: var(--paper);
  }
  .person-role {
    left: 19px;
    top: 111px;
    font-size: 11px;
    color: var(--paper);
  }
  .company-name {
    left: 176px;
    top: 94px;
    font-size: 16px;
    font-weight: 700;
    color: var(--brand-blue);
  }
  .contact {
    font-size: 11px;
    color: var(--text-grey);
    left: 176px;
  }
  .front-brand {
    position: absolute;
    left: 231px;
    top: 14px;
    width: 94px;
    height: 60px;
    display: flex;
    align-items: center;
    justify-content: center;
    font-size: 11px;
    font-weight: 700;
    color: var(--brand-blue);
  }
  .brands-title {
    left: 0;
    width: 100%;
    text-align: center;
    top: 14px;
    font-size: 14px;
    color: var(--paper);
  }
  .brand-mark {
    position: absolute;
    top: 60px;
    width: 130px;
    height: 62px;
    display: flex;
    align-items: center;
    justify-content: center;
    font-size: 13px;
    font-weight: 700;
    color: var(--paper);
  }
  .brand-mark--jobs { left: 37px; }
  .brand-mark--fair { left: 185px; }
  .placeholder {
    position: absolute;
    top: 142px;
    width: 130px;
    text-align: center;
    font-size: 19px;
    font-weight: 700;
    line-height: 23px;
    color: var(--paper);
  }
  .placeholder--jobs { left: 29px; }
  .placeholder--fair { left: 202px; }
</style>
</head>
<body>
  <section class="card card--front">
    <svg class="front-arc" width="342" height="221" viewBox="0 0 342 221" aria-hidden="true">
      <path d="M0 0 H118 A157 157 0 0 1 111 221 H0 Z"/>
    </svg>
    <div class="front-brand">Wachwechselpunkt</div>
    <p class="line person-name">Paul Beispiel</p>
    <p class="line person-role">Geschäftsführer</p>
    <p class="line company-name">KLO GmbH</p>
    <p class="line contact" style="top:116px">Lindenweg 7</p>
    <p class="line contact" style="top:130px">86650 Auheim</p>
    <p class="line contact" style="top:148px">Telefon 08431 - 512 30 77</p>
    <p class="line contact" style="top:163px">Mobil 0176 - 318 52 904</p>
    <p class="line contact" style="top:182px">info@wachwechselpunkt.de</p>
    <p class="line contact" style="top:196px">www.wachwechselpunkt.de</p>
  </section>

  <section class="card card--back">
    <p class="line brands-title">Unsere Marken</p>
    <div class="brand-mark brand-mark--jobs">Wachwechselpunkt</div>
    <div class="brand-mark brand-mark--fair">Marvento</div>
    <p class="placeholder placeholder--jobs">Logo<br>Platzhalter</p>
    <p class="placeholder placeholder--fair">Logo<br>Platzhalter</p>
  </section>
</body>
</html>
```